Must Be Creative: Trade Show Booth for HR Conference 10x10

Design Style: high-level professional - a bit playful with our theme (read the theme) please be very creative...not boring...eye catching design that will make folks stop and think...We are going for bold. Look at the examples uploaded to this brief. Stick with clean designs professional.

Audience: HR and Talent Leaders

Size 10x10 - (114x91 - safe area 104x81)
we are not doing a podium - do not include it in your design.

Brand: Vantage Growth Studio - do not use our logo in the design. We will decide how and where to add the logo and QR code when we are done with the design. Make sure your design can accommodate a QR Code and our logo.

Brand Colors:
Navy Blue: #003366
Represents: Trust, stability, and professionalism.
Emerald Green: #009473
Represents: Growth, renewal, and prosperity. It also conveys a sense of balance and calm.
Deep Charcoal: #333333
Represents: Sophistication and strength, providing a solid background that makes other colors stand out.
Vibrant Orange: #FF6A00
Represents: Energy, enthusiasm, and warmth. It's an engaging color that can stimulate action and interaction.

FONT: bold face but soft font
Montserrat:
Roboto:
Lato:
Open Sans:

Theme Text:
Are Your Managers Driving Talent Away?
Tagline:
We Empower Leaders to Retain Talent

What we do: (Do not use "What we do text)
(This text can be included or excluded)
Equip Leaders
Engage Teams
Retain Top Talent
Ignite Inclusive Leadership

Imagine Must be Diverse Teams: (See images we uploaded)

Collaborative Teams: An image of a diverse group of professionals engaged in a collaborative work setting. This could be a roundtable discussion or a team actively engaging in a brainstorming session. Such an image would illustrate inclusivity and the dynamic interactions your training promotes.

Empowering Leadership: Consider an image that depicts a leader in action, possibly mentoring or guiding a team member. Showing a moment of teaching or a supportive interaction can powerfully convey the concept of "empower".

Inspirational Settings: An image that includes open, inviting workspace environments that suggest transparency and openness. Spaces that encourage free exchange of ideas can metaphorically represent an inclusive and engaging leadership style.

Success and Achievement: An image that captures a moment of celebration within a team—perhaps cheering or a congratulatory setting—can effectively illustrate the outcome of effective leadership and team retention.

Please ask any questions you have about this project. I've tried to paint the picture as well as I can.

Target Market(s)

HR and Talent Managers

Industry/Entity Type

Human Resources

Font styles to use
Serif
Sans Serif
Decorative

Colors
0054AA
0677BA
7BADD7
CADEEF
E8F1F8
0094D4
00A9DD
6FCCEA
C7EBF8
E9F6FB
00AB8E
00BBA5
67D7C9
C6EFE9
E9F9F6
F0912C
F2A743
F7CA91
FBE8D2
FDF5EE
EB3D1F
EC4F4E
F09395
F8D3D4
FCEDEE

Requirements
Must have
• creative design ideas
Nice to have
• incorporating the photo into the theme
Should not have
• Do not add our logo. We did not include it in the brief - we may add the logo later

```html
<!DOCTYPE html>
<html lang="en">
<head>
<meta charset="utf-8">
<title>Trade Show Booth – Are Your Managers Driving Talent Away?</title>
<link rel="stylesheet" href="https://fonts.googleapis.com/css2?family=Montserrat:wght@300;400;700&family=Open+Sans:ital,wght@0,600;0,700;1,600&display=swap">
<style>
  :root {
    --stage: #e9e7df;
    --navy: #003366;
    --navy-deep: #0d1a3d;
    --lavender: rgba(152, 160, 232, 0.72);
    --orange: #f0912c;
    --orange-bright: #ff6a00;
    --white: #ffffff;
    --photo-warm: #b98a6d;
    --photo-light: #d9d6dc;
    --photo-dark: #3a3340;
  }
  * { box-sizing: border-box; margin: 0; padding: 0; }
  html, body {
    width: 1200px; height: 1200px; overflow: hidden;
    background: var(--stage);
  }
  .booth {
    position: absolute; left: 40px; top: 152px;
    width: 1120px; height: 896px; overflow: hidden;
  }
  .booth__photo {
    position: absolute; inset: 0;
    background:
      radial-gradient(ellipse at 70% 45%, var(--photo-light) 0%, rgba(217,214,220,0) 45%),
      linear-gradient(100deg, var(--photo-light) 0%, #c9c2c4 40%, var(--photo-warm) 75%, var(--photo-dark) 100%);
  }
  .booth__overlay { position: absolute; inset: 0; width: 100%; height: 100%; }
  .headline {
    position: absolute; left: 54px; top: 132px;
    font-family: "Montserrat", sans-serif; color: var(--white);
    text-transform: uppercase; line-height: 1;
  }
  .headline span { display: block; }
  .headline__light { font-weight: 300; font-size: 84px; letter-spacing: 1px; }
  .headline__mid { font-weight: 400; font-size: 44px; margin: 8px 0 10px; letter-spacing: 1px; }
  .headline__bold { font-weight: 700; font-size: 64px; margin-bottom: 4px; }
  .tagline {
    position: absolute; left: 0; top: 440px;
    width: 700px; height: 46px;
    background: var(--orange);
    clip-path: polygon(0 0, 100% 0, 96% 100%, 0 100%);
    font-family: "Open Sans", sans-serif; font-style: italic; font-weight: 600;
    font-size: 28px; color: var(--white);
    line-height: 46px; padding-left: 50px;
  }
  .services {
    position: absolute; left: 58px; top: 600px;
    list-style: none;
    font-family: "Open Sans", sans-serif; font-weight: 700;
    font-size: 32px; color: var(--white);
    text-transform: uppercase; letter-spacing: 1px;
  }
  .services::before {
    content: ""; position: absolute; left: 13px; top: 30px; bottom: 30px;
    width: 1px; background: rgba(255,255,255,0.5);
  }
  .services__item {
    position: relative; padding-left: 58px; height: 60px; line-height: 60px;
  }
  .services__item::before {
    content: ""; position: absolute; left: 2px; top: 18px;
    width: 22px; height: 22px; border-radius: 50%;
    border: 1.5px solid rgba(255,255,255,0.7);
  }
</style>
</head>
<body>
  <section class="booth">
    <div class="booth__photo" role="img" aria-label="Photo of a diverse, smiling team joining hands in a celebratory high-five in a bright office with brick walls"></div>
    <svg class="booth__overlay" viewBox="0 0 1120 896" preserveAspectRatio="none" aria-hidden="true">
      <defs>
        <linearGradient id="navyFade" x1="0" y1="0" x2="0" y2="1">
          <stop offset="0.45" stop-color="#0d1a3d" stop-opacity="0"/>
          <stop offset="1" stop-color="#0d1a3d" stop-opacity="0.9"/>
        </linearGradient>
      </defs>
      <polygon points="0,0 1040,0 420,896 0,896" fill="rgba(152,160,232,0.72)"/>
      <polygon points="0,380 640,540 420,896 0,896" fill="url(#navyFade)"/>
      <polygon points="1040,0 1120,0 1120,80 990,230" fill="#f0912c" opacity="0.75"/>
      <polygon points="1120,460 1120,896 1000,896" fill="#0d1a3d" opacity="0.35"/>
    </svg>

    <h1 class="headline">
      <span class="headline__light">Are</span>
      <span class="headline__mid">Your Managers</span>
      <span class="headline__bold">Driving Talent</span>
      <span class="headline__light">Away?</span>
    </h1>

    <p class="tagline">We Empower Leaders to Retain Talent</p>

    <ul class="services">
      <li class="services__item">Equip Leaders</li>
      <li class="services__item">Engage Teams</li>
      <li class="services__item">Retain Top Talent</li>
      <li class="services__item">Ignite Inclusive Leadership</li>
    </ul>
  </section>
</body>
</html>
```